Stonebell Inc Ad Design, trying to attract new customers

Please see attached pictures and files for information
We are a Class A - Residential General Contractor in Lynchburg, VA with Master HVAC and Master PLUMBING Licenses. We focus on Water and Air Solutions for property owners.
We build, remodel, and repair homes
We do HVAC, including Humidity Control and Air Purification
We do Plumbing
We love to fix Water Leaks for Plumbing, Roof Leaks, Skylight Leaks, Basement Leaks, Foundation Leaks, Door and Window Leaks
We solve water and air issues on the outside of properties with custom structures, grading, and landscaping

Target Market(s)

Residential and Light Commercial property owners

Industry/Entity Type

Construction

Font styles to use
Other font styles liked:
• see cards

Colors
0054AA
0677BA
7BADD7
CADEEF
E8F1F8
00AB8E
00BBA5
67D7C9
C6EFE9
E9F9F6

Requirements
Must have
• See business cards
Nice to have
• see business cards
Should not have
• My name

```html
<!DOCTYPE html>
<html lang="en">
<head>
<meta charset="utf-8">
<title>Stonebell Inc – Water and Air Solutions</title>
<link rel="stylesheet" href="https://fonts.googleapis.com/css2?family=Merriweather:wght@900&family=Crimson+Pro:wght@400&display=swap">
<style>
  :root {
    --page-bg: #a6a6a6;
    --banner-white: #ffffff;
    --brand-green: #7ab842;
    --brand-blue: #1b8fd2;
    --logo-blue: #0677ba;
    --photo-light: #c9ccce;
    --photo-mid: #8e959b;
    --photo-dark: #4d555c;
    --body-ink: #1e1e1e;
  }
  * { margin: 0; padding: 0; box-sizing: border-box; }
  html, body {
    width: 1200px;
    height: 1200px;
    overflow: hidden;
    background: var(--page-bg);
  }
  .canvas {
    width: 1200px;
    height: 1200px;
    display: flex;
    align-items: center;
    justify-content: center;
  }
  .banner {
    width: 1120px;
    height: 559px;
    display: block;
    background: var(--banner-white);
  }
  .banner__headline {
    font-family: "Merriweather", Georgia, serif;
    font-weight: 900;
    fill: var(--banner-white);
  }
  .banner__headline--small { font-size: 49px; }
  .banner__headline--large { font-size: 86px; }
  .banner__brand {
    font-family: "Crimson Pro", "Times New Roman", serif;
    font-size: 22px;
    fill: var(--logo-blue);
  }
  .banner__services {
    font-family: "Crimson Pro", "Times New Roman", serif;
    font-size: 10.6px;
    fill: var(--body-ink);
  }
  .band-blue { fill: var(--brand-blue); }
  .band-green { fill: var(--brand-green); }
</style>
</head>
<body>
<main class="canvas">
  <svg class="banner" viewBox="0 0 804 401" preserveAspectRatio="xMidYMid meet" aria-label="Stonebell Inc advertisement banner">
    <defs>
      <linearGradient id="photo-tones" x1="0" y1="0" x2="1" y2="1">
        <stop offset="0" stop-color="var(--photo-light)"/>
        <stop offset="0.55" stop-color="var(--photo-mid)"/>
        <stop offset="1" stop-color="var(--photo-dark)"/>
      </linearGradient>
    </defs>

    <rect class="banner__base" x="0" y="0" width="804" height="401" fill="var(--banner-white)"/>

    <polygon class="banner__photo" role="img"
      aria-label="Photo of technicians installing ductwork on a ladder and a plumber fitting pipes"
      points="457,66 787,106 657,366 322,241" fill="url(#photo-tones)"/>
    <line x1="572" y1="246" x2="657" y2="366" stroke="var(--banner-white)" stroke-width="2"/>

    <polygon class="band-blue" points="0,0 522,0 457,66"/>
    <polygon class="band-green" points="0,0 457,66 572,246 0,234"/>

    <text class="banner__brand" x="632" y="84" text-anchor="middle">Stonebell Inc</text>

    <text class="banner__headline banner__headline--small" x="30" y="124">Water and Air</text>
    <text class="banner__headline banner__headline--large" x="28" y="207">Solutions</text>

    <text class="banner__services">
      <tspan x="30" y="301">We build, remodel, and repair homes</tspan>
      <tspan x="30" y="314.5">We do HVAC, including Humidity Control and Air Purification</tspan>
      <tspan x="30" y="328">We do Plumbing</tspan>
      <tspan x="30" y="341.5">We love to fix Water Leaks for Plumbing, Roof Leaks, Skylight Leaks, Basement Leaks, Foundation Leaks,</tspan>
      <tspan x="30" y="355">Door and Window Leaks</tspan>
      <tspan x="30" y="368.5">We solve water and air issues on the outside of properties with custom structures, grading, and landscaping</tspan>
    </text>
  </svg>
</main>
</body>
</html>
```